Web Design Project for Copperleaf Systems Collective

Design a webpage to replace www.copperleafsystemscollective.com.au

View the website and design a new website based on the same philosophy of the original.

The website will be fresh, simple, elegant, modern, and a hint of high degree of technical backdrop.

Please utilise the logo in the website design and keep the different contents.

Industry/Entity Type

Group

Requirements
Must have
• Must incorporate the logo which will be uploaded.

```html
<!DOCTYPE html>
<html lang="en">
<head>
<meta charset="utf-8">
<title>Copperleaf Systems Collective</title>
<link rel="stylesheet" href="https://fonts.googleapis.com/css2?family=Arimo:wght@400;700&family=Open+Sans:wght@700&display=swap">
<style>
:root{
  --ink:#555555;
  --accent:#c0221b;
  --navy:#2e3592;
  --hero-top:#5b64b2;
  --hero-bottom:#2a3387;
  --card-light:#8b91c6;
  --card-dark:#2f3a93;
  --panel:#f2f2f2;
  --footer:#222222;
  --white:#ffffff;
}
*{box-sizing:border-box;margin:0;padding:0}
html,body{width:1200px;height:1087px;overflow:hidden;background:var(--white);font-family:Arimo,Arial,sans-serif}
.page{position:relative;width:1200px;height:1087px}

.site-header{position:absolute;left:0;top:0;width:1200px;height:146px}
.brand{position:absolute;left:49px;top:40px;display:flex;align-items:center;gap:12px}
.brand-mark{width:44px;height:44px;border-radius:50%;background:var(--navy)}
.brand-name{font-family:'Open Sans',Arial,sans-serif;font-weight:700;font-size:21px;color:var(--navy);line-height:1}
.main-nav{position:absolute;right:46px;top:62px;display:flex;gap:29px}
.main-nav a{font-weight:700;font-size:21px;color:var(--ink);text-decoration:none}
.main-nav a.current{color:var(--accent);text-decoration:underline}

.hero{position:absolute;left:0;top:146px;width:1200px;height:331px;background:linear-gradient(180deg,var(--hero-top),var(--hero-bottom));box-shadow:0 2px 5px rgba(0,0,0,.35)}
.hero-title{position:absolute;left:67px;top:26px;font-family:'Open Sans',Arial,sans-serif;font-size:21px;font-weight:700;color:var(--white)}
.hero-copy{position:absolute;left:48px;top:63px;width:692px;height:211px;border-radius:8px;background:rgba(20,28,110,.18);padding:10px 19px;font-size:15.3px;line-height:28px;color:var(--white)}
.hero-more{position:absolute;left:67px;top:294px;font-size:15px;font-weight:700;color:var(--white);text-decoration:underline}
.hero-globe{position:absolute;left:846px;top:42px;width:236px;height:236px;border-radius:50%;background:radial-gradient(circle at 40% 35%,#ffffff,#c9ccd8 60%,#8f94aa);box-shadow:4px 6px 10px rgba(0,0,0,.35)}

.feature-card{position:absolute;top:516px;width:328px;height:237px;border-radius:7px;background:linear-gradient(90deg,var(--card-light),var(--card-dark));box-shadow:0 0 4px rgba(0,0,0,.35);color:var(--white);overflow:hidden}
.feature-card h2{position:absolute;left:19px;top:15px;font-size:21px;font-weight:700}
.feature-card .rule{position:absolute;left:19px;top:49px;width:193px;height:1px;background:rgba(255,255,255,.55)}
.feature-card p{position:absolute;left:19px;top:66px;width:198px;font-size:15.3px;line-height:20px}
.feature-card .card-more{position:absolute;right:0;bottom:0;width:118px;height:33px;border-radius:8px 0 0 0;background:rgba(255,255,255,.12);font-size:12.5px;font-weight:700;line-height:35px;text-align:center;color:var(--white);text-decoration:none}
.card-reflection{position:absolute;top:759px;width:328px;height:64px;border-radius:8px 8px 0 0;background:linear-gradient(180deg,rgba(60,70,150,.14),rgba(255,255,255,0));}
.c1{left:48px}.c2{left:436px}.c3{left:824px}

.partners{position:absolute;left:0;top:826px;width:1200px;height:191px;background:var(--panel);border-top:2px solid #dedede}
.partners h2{position:absolute;left:47px;top:21px;font-family:'Open Sans',Arial,sans-serif;font-size:23px;font-weight:700;color:var(--navy)}
.partner-row{position:absolute;left:0;top:74px;width:1200px;height:67px}
.partner-row svg{position:absolute;top:0}
.partner-badge{position:absolute;top:5px;height:58px;border-radius:6px;background:#d9dbe6}

.site-footer{position:absolute;left:0;top:1017px;width:1200px;height:70px;background:var(--footer);font-size:14px}
.footer-nav{position:absolute;left:48px;top:29px;color:#8a8a8a}
.footer-nav a{color:#8a8a8a;text-decoration:none}
.footer-nav a.current{color:var(--white)}
.copyright{position:absolute;right:47px;top:31px;font-size:12.5px;color:#8a8a8a}
</style>
</head>
<body>
<div class="page">
  <header class="site-header">
    <div class="brand"><span class="brand-mark"></span><span class="brand-name">Copperleaf Systems Collective</span></div>
    <nav class="main-nav">
      <a href="#">Home</a><a href="#" class="current">Contact</a><a href="#">Online Shop</a><a href="#">Blog</a>
    </nav>
  </header>

  <section class="hero">
    <h1 class="hero-title">Copperleaf Systems Collective</h1>
    <div class="hero-copy">Lorem ipsum dolor sit amet, consectetuer adipiscing elit. Aenean commodo ligula eget dolor. Aenean massa. Cum sociis natoque penatibus et magnis dis parturient montes, nascetur ridiculus mus. Donec quam felis, ultricies nec, pellentesque eu, pretium quis, sem. Nulla consequat massa quis enim. Donec pede justo, fringilla vel, aliquet nec, vulputate eget, arcu. In enim justo, rhoncus ut, imperdiet a, venenatis vitae, justo. Nullam dictum felis eu pede mollis pretium. Integer tincidunt.</div>
    <a class="hero-more" href="#">Read More</a>
    <div class="hero-globe" role="img" aria-label="Wireframe globe showing Asia and Australia"></div>
  </section>

  <article class="feature-card c1">
    <h2>Mission</h2><span class="rule"></span>
    <p>Our mission is to assist in society by providing a unified network of solutions that add value for our customers.</p>
    <a class="card-more" href="#">READ MORE</a>
  </article>
  <article class="feature-card c2">
    <h2>Services</h2><span class="rule"></span>
    <p>Copperleaf Systems Collective Supply, Install and service the complete range of Electrical and communications equipment. We provide services to suit your requirements.</p>
    <a class="card-more" href="#">READ MORE</a>
  </article>
  <article class="feature-card c3">
    <h2>Products</h2><span class="rule"></span>
    <p>Lorem ipsum dolor sit amet, consectetuer adipiscing elit. Aenean commodo ligula eget dolor. Aenean massa.</p>
    <a class="card-more" href="#">READ MORE</a>
  </article>
  <div class="card-reflection c1"></div>
  <div class="card-reflection c2"></div>
  <div class="card-reflection c3"></div>

  <section class="partners">
    <h2>Our Partners</h2>
    <div class="partner-row">
      <svg style="left:47px" width="28" height="52" viewBox="0 0 28 52"><path d="M24 2 L6 26 L24 50" fill="none" stroke="#9a9a9a" stroke-width="7"/></svg>
      <div class="partner-badge" style="left:82px;width:218px"></div>
      <div class="partner-badge" style="left:338px;width:174px"></div>
      <div class="partner-badge" style="left:548px;width:92px"></div>
      <div class="partner-badge" style="left:672px;width:178px"></div>
      <div class="partner-badge" style="left:886px;width:132px"></div>
      <div class="partner-badge" style="left:1043px;width:68px;border-radius:50%;height:68px;top:0"></div>
      <svg style="left:1126px" width="28" height="52" viewBox="0 0 28 52"><path d="M4 2 L22 26 L4 50" fill="none" stroke="#dcdcdc" stroke-width="7"/></svg>
    </div>
  </section>

  <footer class="site-footer">
    <nav class="footer-nav"><a href="#" class="current">home</a> | <a href="#">mission</a> | <a href="#">services</a> | <a href="#">products</a> | <a href="#">partners</a> | <a href="#">contact</a> | <a href="#">online shop</a> | <a href="#">blog</a></nav>
    <p class="copyright">Website © Copperleaf Systems Collective Pty Ltd. All Rights Reserved</p>
  </footer>
</div>
</body>
</html>
```